Restaurant menu design

I need a menu for a restaurant in Spain.
It has to be bohemian but modern. We need something romantic and elegant.
The restaurant is elegant with good food and an excellent reputation. It is also modern at the same time.
The restaurant is superbly decorated and very chick so we need something "class" to fit in with the surroundings.
The size of the document must be 325 mm in high and 245 mm as a maximum and preferably made in indesign.

Reason: Thank you all for your designs.
So far all your designs are ok but it isn´t what we are looking for. Most of the designs are too loaded, too many colors and too much decoration.

Target Market(s)

Adults of various age groups and different nationalities mostly European.

Industry/Entity Type

Restaurant

Requirements
Must have
• The menu must have two interior pages with the text as in the document attached.It must be easily legible.
Nice to have
• See what kind of menus they use in important restaurants in places like Paris, see what designs are in trend, but Not necessarily doing the same style if it doesn’t fit in with the description above.
Should not have
• Nothing old fashioned.

```html
<!DOCTYPE html>
<html lang="es">
<head>
<meta charset="utf-8">
<title>Le Velours — Carta</title>
<link rel="stylesheet" href="https://fonts.googleapis.com/css2?family=Source+Sans+3:wght@300;400&display=swap">
<style>
  :root {
    --page: #ffffff;
    --band-light: #c9a398;
    --band-dark: #b3897a;
    --heading: #9b6b92;
    --text: #1e1e1e;
  }
  * { margin: 0; padding: 0; box-sizing: border-box; }
  html, body { width: 904px; height: 1200px; overflow: hidden; background: var(--page); }
  .menu-page {
    position: relative;
    width: 904px;
    height: 1200px;
    background: var(--page);
    font-family: "Source Sans 3", "Helvetica Neue", Arial, sans-serif;
    color: var(--text);
  }
  .side-band {
    position: absolute; top: 0; left: 0;
    width: 112px; height: 100%;
    background: var(--band-light);
  }
  .side-band-edge {
    position: absolute; top: 0; left: 112px;
    width: 17px; height: 100%;
    background: var(--band-dark);
  }
  .menu-section {
    position: absolute;
    left: 216px;
    width: 520px;
  }
  .section-title {
    font-weight: 300;
    font-size: 51px;
    line-height: 1;
    color: var(--heading);
    letter-spacing: 0.2px;
    margin-bottom: 26px;
  }
  .dish-list { list-style: none; }
  .dish {
    display: flex;
    height: 32.8px;
    align-items: center;
    font-size: 16px;
    font-weight: 400;
  }
  .dish-name { width: 417px; }
  .dish-price { white-space: nowrap; }
  .section-starters { top: 103px; }
  .section-grill { top: 629px; }
  .section-kids { top: 991px; }
  .brand-name {
    position: absolute;
    left: 800px;
    top: 1108px;
    font-size: 18px;
    font-weight: 400;
    color: var(--heading);
    display: flex;
    align-items: center;
    gap: 6px;
  }
  .brand-dot {
    width: 8px; height: 8px; border-radius: 50%;
    background: var(--heading);
  }
</style>
</head>
<body>
<main class="menu-page">
  <div class="side-band"></div>
  <div class="side-band-edge"></div>

  <section class="menu-section section-starters">
    <h2 class="section-title">Entradas</h2>
    <ul class="dish-list">
      <li class="dish"><span class="dish-name">Ensalada Le Velours. Lechuga, tomate.</span><span class="dish-price">7,75 €</span></li>
      <li class="dish"><span class="dish-name">Ensalada Caprese (Tomate y Mozzarella).</span><span class="dish-price">7,75 €</span></li>
      <li class="dish"><span class="dish-name">Escarola al Queso de Cabra con Bacon.</span><span class="dish-price">6,75 €</span></li>
      <li class="dish"><span class="dish-name">Cocktail de Gambas, Langostinos y Aguacate.</span><span class="dish-price">7,50 €</span></li>
      <li class="dish"><span class="dish-name">La Sopa de Pescado.</span><span class="dish-price">8,25 €</span></li>
      <li class="dish"><span class="dish-name">Crema de Espárragos Trigueros y Calabacín.</span><span class="dish-price">5,95 €</span></li>
      <li class="dish"><span class="dish-name">Carpaccio de Ternera.</span><span class="dish-price">11,50 €</span></li>
      <li class="dish"><span class="dish-name">Carpaccio de Salmón al Eneldo.</span><span class="dish-price">9,75 €</span></li>
      <li class="dish"><span class="dish-name">Carpaccio de Atún.</span><span class="dish-price">13,95 €</span></li>
      <li class="dish"><span class="dish-name">Melón con Jamón Ibérico.</span><span class="dish-price">9,25 €</span></li>
      <li class="dish"><span class="dish-name">Parrillada de Verduras.</span><span class="dish-price">7,95 €</span></li>
      <li class="dish"><span class="dish-name">Parrillada de Verduras Gratinada al Queso de Cabra.</span><span class="dish-price">8,95 €</span></li>
      <li class="dish"><span class="dish-name">Gambas Roja de la Bahía.</span><span class="dish-price">12,95 €</span></li>
    </ul>
  </section>

  <section class="menu-section section-grill">
    <h2 class="section-title">Pescados al Grill</h2>
    <ul class="dish-list">
      <li class="dish"><span class="dish-name">Lubina al Hinojo.</span><span class="dish-price">15,50 €</span></li>
      <li class="dish"><span class="dish-name">Lubina Fileteada y su Salsa Rústica con Berenjena.</span><span class="dish-price">18,50 €</span></li>
      <li class="dish"><span class="dish-name">Filete de Rodaballo y su Salsa de Marisco.</span><span class="dish-price">17,25 €</span></li>
      <li class="dish"><span class="dish-name">Dorada del Mediterráneo.</span><span class="dish-price">13,95 €</span></li>
      <li class="dish"><span class="dish-name">Lenguado al Grill con Hierbas Provenzales.</span><span class="dish-price">20,75 €</span></li>
      <li class="dish"><span class="dish-name">Pieza de Atún Fresco y su Salsa Griega.</span><span class="dish-price">18,95 €</span></li>
      <li class="dish"><span class="dish-name">Lomo de Salmón con Salsa de Frambuesa.</span><span class="dish-price">11,25 €</span></li>
      <li class="dish"><span class="dish-name">Parrillada de Pescado y Marisco.</span><span class="dish-price">23,505 €</span></li>
    </ul>
  </section>

  <section class="menu-section section-kids">
    <h2 class="section-title">Especial Niños</h2>
    <ul class="dish-list">
      <li class="dish"><span class="dish-name">Solomillo Junior, huevo y patatas fritas.</span><span class="dish-price">6,25 €</span></li>
      <li class="dish"><span class="dish-name">Fish &amp; chips.</span><span class="dish-price">6,25 €</span></li>
    </ul>
  </section>

  <div class="brand-name"><span class="brand-dot"></span>Le Velours</div>
</main>
</body>
</html>
```